New young doctors office business card

Doctor's office
Hello:
My name is Dr. Mateo Anselmo Quiroga Benítez. I need a business card for my new office located within a hospital. The name of the hospital is "Hospital Almendral". Although the hospital logo and name must be included in the business card, please make me a personal logo for myself. The logo might be maybe my name in a stylish font, or my initials (MAQB) or something like that. Im more inclined to a font logo, rather than a image logo, but a good one might change my mind. The info on my business card is going to be in spanish. The following info must be included please (the info within parenthesis is not to be included, it is provided for you to understand it since it's in spanish, so you can properly place it on the card):
-Dr. Mateo Anselmo Quiroga Benítez (my name)
-Medicina general (My specialty)
-Hospital Almendral (The name of the hospital where my office is)
-Calle Tomás Ibarrola #527 Col. Peñascal (address)
-Tel 471-5836 (Office phone)
-Sábado y domingo 10:00 am a 10:00pm (Office hours)
-Emergencias: 613-907-5148 (Emergency phone)
-mateoqb@correoandino.net (email)
-English Spoken
So, that's all the info i need to be on the business card. Although it's a business card for a doctor's office, i dont want it to be a boring, plain business card. Make it eye-catchy and stylish please. As i said, the hospital logo must be included. You'll find it on the heading of the PDF file i attached, but dont make it the center of attention.
Physician
Hello:My name is Dr. Mateo Anselmo Quiroga Benítez. I need a business card for my new office located within a hospital. The name of the hospital is "Hospital Almendral". Although the hospital logo and name must be included in the business card, please make me a personal logo for myself. The logo might be maybe my name in a stylish font, or my initials (MAQB) or something like that. Im more inclined to a font logo, rather than a image logo, but a good one might change my mind. The info on my business card is going to be in spanish. The following info must be included please (the info within parenthesis is not to be included, it is provided for you to understand it since it's in spanish, so you can properly place it on the card):-Dr. Mateo Anselmo Quiroga Benítez (my name)-Medicina general (My specialty)-Hospital Almendral (The name of the hospital where my office is)-Calle Tomás Ibarrola #527 Col. Peñascal (address)-Tel 471-5836 (Office phone)-Sábado y domingo 10:00 am a 10:00pm (Office hours)-Emergencias: 613-907-5148 (Emergency phone)-mateoqb@correoandino.net (email)-English Spoken So, that's all the info i need to be on the business card. Although it's a business card for a doctor's office, i dont want it to be a boring, plain business card. Make it eye-catchy and stylish please. As i said, the hospital logo must be included. You'll find it on the heading of the PDF file i attached, but dont make it the center of attention.

```html
<!DOCTYPE html>
<html lang="es">
<head>
<meta charset="utf-8">
<title>Tarjeta de presentación — Dr. Mateo Anselmo Quiroga Benítez</title>
<link rel="stylesheet" href="https://fonts.googleapis.com/css2?family=Source+Sans+3:wght@300;400;600;700&display=swap">
<style>
  :root {
    --navy: #1f3c6e;
    --ink: #2b2b2b;
    --paper: #ffffff;
    --backdrop: #dedede;
    --edge: #9a9a9a;
  }
  * { margin: 0; padding: 0; box-sizing: border-box; }
  html, body { width: 1200px; height: 1200px; overflow: hidden; background: var(--backdrop); }
  body { position: relative; font-family: "Source Sans 3", "Myriad Pro", Arial, sans-serif; color: var(--ink); }

  .card { position: absolute; left: 158px; width: 884px; height: 523px; overflow: hidden; }
  .card--front { top: 62px; background: var(--paper); border: 1px solid var(--edge); }
  .card--back { top: 614px; background: var(--navy); }

  .front-shapes { position: absolute; inset: 0; width: 884px; height: 523px; }

  .identity { position: absolute; left: 0; width: 588px; top: 84px; text-align: center; }
  .identity__name { font-weight: 700; font-size: 25.5px; color: var(--navy); letter-spacing: -0.2px; line-height: 1.2; }
  .identity__specialty { font-weight: 400; font-size: 21px; color: var(--ink); line-height: 1.2; margin-top: 2px; }

  .contact { position: absolute; left: 90px; top: 238px; list-style: none; }
  .contact__item { position: absolute; left: 0; display: flex; align-items: center; white-space: nowrap; }
  .contact__icon { width: 38px; height: 34px; flex: none; }
  .contact__text { margin-left: 8px; font-size: 13px; line-height: 1.2; color: var(--ink); }
  .contact__text strong { font-weight: 600; font-size: 14px; display: block; }
  .contact__text--semibold { font-weight: 600; }

  .emblem {
    position: absolute; left: 635px; top: 226px; width: 94px; height: 84px;
    background: radial-gradient(ellipse at center, rgba(255,255,255,0.55), rgba(255,255,255,0.12) 70%);
    border-radius: 6px;
  }

  .hospital-mark { position: absolute; right: 58px; top: 410px; display: flex; align-items: center; gap: 8px; }
  .hospital-mark__square { width: 22px; height: 22px; background: var(--paper); }
  .hospital-mark__name { color: var(--paper); font-weight: 700; font-size: 17px; line-height: 1.05; }

  .monogram {
    position: absolute; left: 0; right: 0; top: 138px; text-align: center;
    color: var(--paper); font-weight: 300; font-size: 100px; line-height: 102px; letter-spacing: 14px;
  }
</style>
</head>
<body>

<section class="card card--front" aria-label="Frente de la tarjeta">
  <svg class="front-shapes" viewBox="0 0 884 523" aria-hidden="true">
    <polygon points="578,0 884,0 884,523 431,523" fill="#1f3c6e"/>
    <line x1="571" y1="0" x2="424" y2="523" stroke="#1f3c6e" stroke-width="3"/>
    <line x1="565" y1="0" x2="415" y2="523" stroke="#1f3c6e" stroke-width="3"/>
  </svg>

  <header class="identity">
    <h1 class="identity__name">Dr. Mateo Anselmo Quiroga Benítez</h1>
    <p class="identity__specialty">Medicina general</p>
  </header>

  <ul class="contact">
    <li class="contact__item" style="top:0">
      <svg class="contact__icon" viewBox="0 0 38 34" aria-hidden="true" fill="none" stroke="#1f3c6e" stroke-width="1.6">
        <path d="M19 25 C13 17 11 13 11 10 a8 8 0 0 1 16 0 c0 3 -2 7 -8 15z"/>
        <circle cx="19" cy="10" r="3"/>
        <path d="M13 22 H8 L3 32 H35 L30 22 H25"/>
      </svg>
      <span class="contact__text"><strong>Hospital Almendral</strong>Calle Tomás Ibarrola #527 Col. Peñascal</span>
    </li>
    <li class="contact__item" style="top:42px">
      <svg class="contact__icon" viewBox="0 0 38 34" aria-hidden="true" fill="#1f3c6e">
        <path d="M2 12 C2 4 36 4 36 12 L36 15 L28 15 L27 11 L11 11 L10 15 L2 15z"/>
        <path d="M11 15 L27 15 L33 31 L5 31z"/>
        <circle cx="19" cy="22" r="3.5" fill="#ffffff"/>
      </svg>
      <span class="contact__text">471-5836</span>
    </li>
    <li class="contact__item" style="top:80px">
      <svg class="contact__icon" viewBox="0 0 38 34" aria-hidden="true" fill="none" stroke="#1f3c6e">
        <circle cx="17" cy="17" r="14" stroke-width="2"/>
        <circle cx="17" cy="17" r="11.5" stroke-width="0.8"/>
        <path d="M17 8 V17 L22 20" stroke-width="1.4"/>
      </svg>
      <span class="contact__text contact__text--semibold">Sábado y domingo 10:00 am a 10:00pm</span>
    </li>
    <li class="contact__item" style="top:119px">
      <svg class="contact__icon" viewBox="0 0 38 34" aria-hidden="true" fill="#1f3c6e">
        <path d="M9 3 L14 3 L16 10 L12.5 13 C14 18 17 21 21 23 L24 19.5 L31 21.5 L31 26 C31 29 28 31 25 30 C15 27 7 19 5 9 C4.5 6 6 3 9 3z"/>
      </svg>
      <span class="contact__text contact__text--semibold">Emergencias: 613-907-5148</span>
    </li>
    <li class="contact__item" style="top:157px">
      <svg class="contact__icon" viewBox="0 0 38 34" aria-hidden="true" fill="none" stroke="#1f3c6e" stroke-width="1.6">
        <rect x="6" y="9" width="25" height="16"/>
        <path d="M6 9 L18.5 19 L31 9 M6 25 L15 16 M31 25 L22 16"/>
      </svg>
      <span class="contact__text">mateoqb@correoandino.net</span>
    </li>
    <li class="contact__item" style="top:188px">
      <svg class="contact__icon" viewBox="0 0 38 34" aria-hidden="true" fill="none" stroke="#1f3c6e" stroke-width="1.6">
        <path d="M12 29 L12 25 C7 23 5 19 6 14 C7 8 12 5 17 6 C22 7 24 11 23 15 L25 19 L22 19 L22 23 L17 24 L17 29"/>
        <path d="M27 14 q3 4 0 8 M30 11 q5 7 0 14"/>
      </svg>
      <span class="contact__text">English Spoken</span>
    </li>
  </ul>

  <div class="emblem" role="img" aria-label="Emblema médico del caduceo en blanco"></div>

  <div class="hospital-mark">
    <span class="hospital-mark__square"></span>
    <span class="hospital-mark__name">Hospital<br>Almendral</span>
  </div>
</section>

<section class="card card--back" aria-label="Reverso de la tarjeta">
  <p class="monogram">MA<br>QB</p>
</section>

</body>
</html>
```